massage therapy Business Card Design

massage therapy business card
I would like a custom logo created as well.
My vision is angel wings with the HB business initials in between them.
A very simple design.
Colors preferred are light blues and greens.

Target Market(s)

Massage, Spa, fitness

Industry/Entity Type

Massage Therapy

Contact Information for Business Card

A Harbor Breeze
Nora Campe
Massage Therapist and Veldane Pulse Method Practitioner
2870 Marlow Ridge Road, Conway, AR 72039
501-384-6190
nora.harborbreeze@mailvinto.com

Colors
abd036
33a6d7
3176b5
0255a3
0392cd
9bcb3c
cadf82

Requirements
Must have
• the logo must have angel wing.

```html
<!DOCTYPE html>
<html lang="en">
<head>
<meta charset="utf-8">
<title>A Harbor Breeze – Business Card</title>
<link rel="stylesheet" href="https://fonts.googleapis.com/css2?family=Bodoni+Moda:wght@400&family=Montserrat:wght@400;500&display=swap">
<style>
  :root {
    --backdrop: #e9ecec;
    --card-teal: #4e7f87;
    --card-mint: #b3fcd0;
    --card-border: #ffffff;
    --ink: #4a4a4a;
    --ink-light: #f4f6f6;
    --shadow: rgba(20, 30, 32, 0.22);
  }
  * { box-sizing: border-box; margin: 0; padding: 0; }
  html, body {
    width: 1200px;
    height: 877px;
    overflow: hidden;
    background: var(--backdrop);
  }
  .canvas {
    width: 1200px;
    height: 877px;
    display: flex;
    flex-direction: column;
    align-items: center;
    justify-content: center;
    gap: 48px;
  }
  .card {
    width: 620px;
    height: 354px;
    box-shadow: 0 12px 30px var(--shadow);
    position: relative;
  }
  .card-back {
    background: var(--card-teal);
    display: flex;
    align-items: center;
    justify-content: center;
  }
  .brand-name {
    font-family: "Bodoni Moda", serif;
    font-weight: 400;
    font-size: 46px;
    letter-spacing: 2px;
    color: var(--ink-light);
  }
  .card-front {
    background: var(--card-border);
    padding: 16px;
  }
  .card-front-inner {
    width: 100%;
    height: 100%;
    background: var(--card-mint);
    position: relative;
    display: flex;
    flex-direction: column;
    align-items: center;
  }
  .person-name {
    margin-top: 78px;
    font-family: "Bodoni Moda", serif;
    font-weight: 400;
    font-size: 58px;
    letter-spacing: 5px;
    color: var(--ink);
    transform: scaleY(1.12);
  }
  .person-role {
    margin-top: 22px;
    font-family: "Montserrat", sans-serif;
    font-weight: 500;
    font-size: 17px;
    line-height: 1.3;
    letter-spacing: 0.6px;
    text-align: center;
    color: var(--ink);
  }
  .contact-line {
    position: absolute;
    left: 18px;
    right: 18px;
    bottom: 20px;
    font-family: "Montserrat", sans-serif;
    font-weight: 500;
    font-size: 10.5px;
    letter-spacing: 0.2px;
    color: var(--ink);
    display: flex;
    justify-content: space-between;
    white-space: nowrap;
  }
</style>
</head>
<body>
  <main class="canvas">
    <section class="card card-back" aria-label="Card back">
      <span class="brand-name">A Harbor Breeze</span>
    </section>

    <section class="card card-front" aria-label="Card front">
      <div class="card-front-inner">
        <h1 class="person-name">NORA CAMPE</h1>
        <p class="person-role">Massage Therapist and Veldane<br>Pulse Method Practitioner</p>
        <p class="contact-line">
          <span class="contact-address">2870 Marlow Ridge Road, Conway, AR 72039</span>
          <span class="contact-phone">501-384-6190</span>
          <span class="contact-email">nora.harborbreeze@mailvinto.com</span>
        </p>
      </div>
    </section>
  </main>
</body>
</html>
```